Front label for Gin bottle - Copper Finch Dusk Gin

We have a initial concept for a label for our new gin which is licorice/aniseed flavor. In the UK there is a famous sweet called twisty bob which has a similar flavor. We are looking for a front label only. You can reference the old label or suggest a completely different design.

Target Market(s)

Male and female gin drinkers in the UK aged 18 to 50.

Font styles to use
Sans Serif

Requirements
Must have
• The Union Jack refers to the UK National Flag and should feature.

```html
<!DOCTYPE html>
<html lang="en">
<head>
<meta charset="utf-8">
<title>Copper Finch Dusk Gin – Front Label</title>
<link href="https://fonts.googleapis.com/css2?family=Oswald:wght@500;600&display=swap" rel="stylesheet">
<style>
  :root {
    --frame: #e6e6e8;
    --navy-deep: #0a0b1c;
    --navy-rich: #0a0a36;
    --flag-light: #24243f;
    --flag-dark: #0b0b26;
    --badge: #ebebed;
    --ink: #14143a;
    --type: #ececf0;
  }
  html, body {
    margin: 0;
    padding: 0;
    overflow: hidden;
    background: var(--frame);
  }
  .label {
    position: relative;
    width: 1200px;
    height: 702px;
    box-sizing: border-box;
    border: 6px solid var(--frame);
    background: linear-gradient(90deg, var(--navy-deep), var(--navy-rich));
    overflow: hidden;
    font-family: "Oswald", "Arial Narrow", sans-serif;
  }
  .flag {
    position: absolute;
    inset: 0;
    width: 100%;
    height: 100%;
  }
  .brand-badge {
    position: absolute;
    left: 497px;
    top: 157px;
    width: 212px;
    height: 212px;
    border-radius: 50%;
    background: var(--badge);
    display: flex;
    align-items: center;
    justify-content: center;
  }
  .brand-name {
    margin: 0;
    color: var(--ink);
    font-weight: 600;
    font-size: 29px;
    line-height: 1.08;
    letter-spacing: 0.5px;
    text-align: center;
    text-transform: uppercase;
  }
  .product {
    position: absolute;
    left: 0;
    right: 0;
    text-align: center;
    color: var(--type);
    margin: 0;
    text-transform: uppercase;
  }
  .product-type {
    top: 385px;
    font-weight: 600;
    font-size: 82px;
    line-height: 1;
    letter-spacing: 1px;
  }
  .tagline {
    top: 484px;
    font-weight: 500;
    font-size: 21px;
    letter-spacing: 0.8px;
  }
  .flavour {
    top: 523px;
    font-weight: 500;
    font-size: 26px;
    letter-spacing: 1px;
    word-spacing: 4px;
  }
</style>
</head>
<body>
  <main class="label">
    <svg class="flag" viewBox="0 0 1188 690" aria-hidden="true">
      <g class="saltire" stroke-linecap="butt">
        <line x1="0" y1="0" x2="1188" y2="690" stroke="var(--flag-light)" stroke-width="100"/>
        <line x1="1188" y1="0" x2="0" y2="690" stroke="var(--flag-light)" stroke-width="100"/>
        <line x1="0" y1="-28" x2="594" y2="317" stroke="var(--flag-dark)" stroke-width="30"/>
        <line x1="594" y1="373" x2="1188" y2="718" stroke="var(--flag-dark)" stroke-width="30"/>
        <line x1="1188" y1="28" x2="594" y2="373" stroke="var(--flag-dark)" stroke-width="30"/>
        <line x1="594" y1="317" x2="0" y2="662" stroke="var(--flag-dark)" stroke-width="30"/>
      </g>
      <g class="cross">
        <rect x="491" y="0" width="204" height="690" fill="var(--flag-light)"/>
        <rect x="0" y="225" width="1188" height="238" fill="var(--flag-light)"/>
        <rect x="532" y="0" width="122" height="690" fill="var(--flag-dark)"/>
        <rect x="0" y="273" width="1188" height="143" fill="var(--flag-dark)"/>
      </g>
    </svg>

    <div class="brand-badge">
      <h1 class="brand-name">Copper<br>Finch<br>Dusk</h1>
    </div>

    <p class="product product-type">Gin</p>
    <p class="product tagline">The Premium Liquor</p>
    <p class="product flavour">Flavour : Aniseed</p>
  </main>
</body>
</html>
```